R & T Welford Carpet & Gutter Cleaning

We clean carpets and have an environmentally friendly gutter machine that cleans out the guttering leaving no mess
Phone 0402718395
or 0413862047

Industry/Entity Type

Business

```html
<!DOCTYPE html>
<html lang="en">
<head>
<meta charset="utf-8">
<title>R &amp; T Welford Carpet &amp; Gutter Cleaning – Business Cards</title>
<link href="https://fonts.googleapis.com/css2?family=Kumbh+Sans:wght@600;700&display=swap" rel="stylesheet">
<style>
  :root {
    --canvas: #ffffff;
    --card-orange: #f26a22;
    --ink-white: #ffffff;
    --tool-tone: #f6ede6;
  }
  * { margin: 0; padding: 0; box-sizing: border-box; }
  html, body {
    width: 1200px;
    height: 1000px;
    overflow: hidden;
    background: var(--canvas);
  }
  .sheet {
    position: relative;
    width: 1200px;
    height: 1000px;
    font-family: "Kumbh Sans", "Helvetica Neue", Arial, sans-serif;
    color: var(--ink-white);
    text-transform: uppercase;
  }
  .card {
    position: absolute;
    background: var(--card-orange);
  }
  .card--portrait { left: 33px; top: 174px; width: 410px; height: 698px; }
  .card--landscape { left: 467px; top: 284px; width: 717px; height: 419px; }

  .brand-name {
    position: absolute;
    font-weight: 700;
    font-size: 43px;
    line-height: 1;
    letter-spacing: 1.5px;
    white-space: nowrap;
  }
  .brand-tagline {
    position: absolute;
    font-weight: 600;
    font-size: 17px;
    line-height: 1;
    letter-spacing: 1.2px;
    white-space: nowrap;
  }
  .service-copy, .contact {
    position: absolute;
    font-weight: 600;
    font-size: 17.5px;
    line-height: 23px;
    letter-spacing: 1px;
    white-space: nowrap;
  }
  .tools-illustration {
    position: absolute;
    display: block;
  }

  /* Portrait card */
  .card--portrait .brand-name,
  .card--portrait .brand-tagline,
  .card--portrait .service-copy,
  .card--portrait .contact {
    left: 0; width: 410px; text-align: center;
  }
  .card--portrait .brand-name { top: 26px; }
  .card--portrait .brand-tagline { top: 65px; }
  .card--portrait .tools-illustration { left: 122px; top: 138px; }
  .card--portrait .service-copy { top: 443px; }
  .card--portrait .contact { top: 578px; }

  /* Landscape card */
  .card--landscape .brand-name,
  .card--landscape .brand-tagline,
  .card--landscape .service-copy,
  .card--landscape .contact {
    right: 38px; text-align: right;
  }
  .card--landscape .brand-name { top: 99px; }
  .card--landscape .brand-tagline { top: 139px; }
  .card--landscape .tools-illustration { left: 71px; top: 78px; }
  .card--landscape .service-copy { top: 174px; }
  .card--landscape .contact { top: 313px; }
</style>
</head>
<body>
<main class="sheet">

  <section class="card card--portrait">
    <h1 class="brand-name">R &amp; T Welford</h1>
    <p class="brand-tagline">Carpet &amp; Gutter Cleaning</p>
    <svg class="tools-illustration" width="168" height="255" viewBox="0 0 168 255" role="img" aria-label="Illustration of a white scrubbing brush and a straw broom standing upright">
      <rect width="168" height="255" fill="var(--tool-tone)" opacity="0.35"/>
    </svg>
    <p class="service-copy">We clean carpets<br>and have an environmentally<br>friendly gutter machine that<br>cleans out the guttering<br>leaving no mess</p>
    <p class="contact">Phone:<br>0402718395<br>or 0413862047</p>
  </section>

  <section class="card card--landscape">
    <h2 class="brand-name">R &amp; T Welford</h2>
    <p class="brand-tagline">Carpet &amp; Gutter Cleaning</p>
    <svg class="tools-illustration" width="172" height="264" viewBox="0 0 172 264" role="img" aria-label="Illustration of a white scrubbing brush and a straw broom standing upright">
      <rect width="172" height="264" fill="var(--tool-tone)" opacity="0.35"/>
    </svg>
    <p class="service-copy">We clean carpets and<br>have an environmentally<br>friendly gutter machine that<br>cleans out the guttering<br>leaving no mess</p>
    <p class="contact">Phone:<br>0402718395<br>or 0413862047</p>
  </section>

</main>
</body>
</html>
```